"The Quiet Harvest" Iwo Jima eulogy discovered by veteran's son.

Project is 6x9 non-fiction history/religion/political paperback for book son wrote. Iwo Jima was the bloodiest battle in Harbor Legion history. The rabbi came to the cemetery prepared to deliver the eulogy (WOKE, DEI) but was banned from doing so by Christian chaplains; thus banning his words. It was a mutiny against their commanding chaplain that cause the cancellation of the planned all-faiths service. It was an antisemitic mutiny by Christian chaplain in time of war; all covered up by the Harbor Legion.

```html
<!DOCTYPE html>
<html lang="en">
<head>
<meta charset="utf-8">
<title>The Quiet Harvest — Book Cover</title>
<link href="https://fonts.googleapis.com/css2?family=Anton&family=Oswald:wght@500;600&display=swap" rel="stylesheet">
<style>
  :root {
    --page-bg: #efefef;
    --cover-bg: #ffffff;
    --title-red: #e31e25;
    --ink: #111111;
    --art-light: #f6f4f1;
    --art-mid: #d9d3ca;
    --art-warm: #c9b89c;
  }
  html, body {
    margin: 0;
    padding: 0;
    width: 1199px;
    height: 1200px;
    overflow: hidden;
    background: var(--page-bg);
  }
  .cover {
    position: absolute;
    left: 250px;
    top: 76px;
    width: 698px;
    height: 1047px;
    display: block;
  }
  .cover-bg { fill: var(--cover-bg); }
  .title {
    font-family: "Anton", "Impact", sans-serif;
    fill: var(--title-red);
  }
  .subtitle {
    font-family: "Oswald", "Arial Narrow", sans-serif;
    font-weight: 600;
    fill: var(--ink);
  }
  .tagline {
    font-family: "Anton", "Impact", sans-serif;
    fill: var(--title-red);
  }
  .blurb {
    font-family: "Oswald", "Arial Narrow", sans-serif;
    font-weight: 500;
    fill: var(--ink);
  }
  .author {
    font-family: "Oswald", "Arial Narrow", sans-serif;
    font-weight: 600;
    fill: var(--title-red);
  }
</style>
</head>
<body>
<svg class="cover" viewBox="0 0 698 1047" xmlns="http://www.w3.org/2000/svg">
  <defs>
    <linearGradient id="art-tone" x1="0" y1="0" x2="0.4" y2="1">
      <stop offset="0" stop-color="var(--art-light)"/>
      <stop offset="0.55" stop-color="var(--art-mid)"/>
      <stop offset="1" stop-color="var(--art-warm)"/>
    </linearGradient>
  </defs>

  <rect class="cover-bg" x="0" y="0" width="698" height="1047"/>

  <text class="title" x="69" y="152" font-size="140" textLength="558" lengthAdjust="spacingAndGlyphs">THE QUIET</text>
  <text class="title" x="82" y="285" font-size="150" textLength="551" lengthAdjust="spacingAndGlyphs">HARVEST</text>

  <text class="subtitle" x="95" y="320" font-size="25" textLength="508" lengthAdjust="spacingAndGlyphs">Iwo Jima Eulogy by Chaplain Rabbi Nathan E. Halberg</text>

  <rect class="cover-art" x="133" y="331" width="403" height="516" rx="4" fill="url(#art-tone)"
        role="img" aria-label="Sketched illustration of a soldier in fatigues planting a waving flag on rocky ground"/>

  <text class="tagline" x="72" y="897" font-size="50" textLength="553" lengthAdjust="spacingAndGlyphs">CHAPLAIN MUTINY AND CONSPIRACY</text>

  <text class="blurb" x="349" y="926" font-size="17" text-anchor="middle" textLength="519" lengthAdjust="spacingAndGlyphs">The untold story of the first Jewish chaplain to serve in the Harbor Legion. Based on</text>
  <text class="blurb" x="349" y="948" font-size="17" text-anchor="middle" textLength="474" lengthAdjust="spacingAndGlyphs">discovery of the only known handwritten copy of his “lost” Iwo Jima eulogy.</text>

  <text class="author" x="349" y="1011" font-size="27" text-anchor="middle" textLength="162" lengthAdjust="spacingAndGlyphs">Theo Marakis</text>
</svg>
</body>
</html>
```